Business card design, sleek & clean . For a notary loan signing business. I work with several lenders escrow officers etc . I am bilingual in Spanish , work 7 days a week to meet clients needs. Loan documents can be emailed for printing.

Logo Text

Not sure sleek clean logo

```html
<!DOCTYPE html>
<html lang="en">
<head>
<meta charset="utf-8">
<title>Marisol Vega – Business Card</title>
<link href="https://fonts.googleapis.com/css2?family=Cinzel:wght@500&family=Montserrat:wght@500;700&family=Open+Sans:wght@400&display=swap" rel="stylesheet">
<style>
  :root {
    --page: #f2f2f4;
    --navy: #1a1f4e;
    --gold: #e2bf6a;
    --white: #ffffff;
  }
  html, body { margin: 0; padding: 0; overflow: hidden; }
  body { width: 1200px; height: 962px; background: var(--page); position: relative; }
  .card { position: absolute; left: 331px; width: 539px; height: 318px; }
  .card--front { top: 129px; background: var(--navy); }
  .card--back { top: 505px; background: var(--white); }

  .brand { position: absolute; left: 0; right: 0; text-align: center; }
  .brand__name {
    font-family: 'Cinzel', serif; font-weight: 500; color: var(--gold);
    margin: 0; line-height: 1; white-space: nowrap;
  }
  .brand__role {
    font-family: 'Montserrat', sans-serif; font-weight: 500; margin: 0;
    text-transform: uppercase; white-space: nowrap;
  }
  .card--front .brand { top: 144px; }
  .card--front .brand__name { font-size: 32px; letter-spacing: 1px; }
  .card--front .brand__role { color: var(--white); font-size: 14px; letter-spacing: 1.6px; margin-top: 13px; }

  .card--back .brand { left: 302px; right: auto; width: 200px; top: 151px; }
  .card--back .brand__name { font-size: 16px; }
  .card--back .brand__role { color: var(--navy); font-size: 10px; letter-spacing: 2.2px; margin-top: 6px; }

  .contact { position: absolute; left: 48px; top: 122px; margin: 0; padding: 0; list-style: none;
    font-family: 'Open Sans', sans-serif; font-size: 13.5px; color: var(--navy); }
  .contact__item { display: flex; align-items: center; height: 23px; }
  .contact__item--bullet { height: 24px; }
  .contact__item--bullet:first-of-type { margin-top: 3px; }
  .contact__icon { width: 16px; height: 16px; margin-right: 8px; flex: none; }
  .contact__dot { width: 6px; height: 6px; border-radius: 50%; background: var(--gold); margin: 2px 13px 0 5px; flex: none; }

  .divider { position: absolute; left: 270px; top: 55px; width: 2px; height: 208px;
    background: linear-gradient(to bottom, rgba(226,191,106,0), var(--gold) 15%, var(--gold) 85%, rgba(226,191,106,0)); }

  .tagline { position: absolute; left: 0; width: 539px; top: 281px; left: 0; text-align: center; margin: 0;
    font-family: 'Montserrat', sans-serif; font-weight: 700; font-size: 9px; color: var(--navy); text-transform: uppercase; }
  .chat-mark { position: absolute; left: 473px; top: 278px; width: 16px; height: 16px; border-radius: 50%; background: var(--navy); }
</style>
</head>
<body>
  <section class="card card--front">
    <div class="brand">
      <p class="brand__name">Marisol Vega</p>
      <p class="brand__role">Notary Public - Loan Signing Agent</p>
    </div>
  </section>

  <section class="card card--back">
    <ul class="contact">
      <li class="contact__item">
        <svg class="contact__icon" viewBox="0 0 16 16" aria-hidden="true">
          <rect width="16" height="16" rx="2" fill="#e2bf6a"/>
          <path d="M5 3.5c-1 .6-1.3 1.6-1 2.8.7 2.6 3 5.3 5.4 6.3 1.1.4 2.2.2 2.9-.7l-1.8-1.9-1.2.8C8 10.2 6.6 8.6 6.1 7.2l1-1L5.8 3.5z" fill="#ffffff"/>
        </svg>(555)014-0237</li>
      <li class="contact__item">
        <svg class="contact__icon" viewBox="0 0 16 16" aria-hidden="true">
          <rect width="16" height="16" rx="2" fill="#e2bf6a"/>
          <rect x="3" y="4.5" width="10" height="7" fill="none" stroke="#ffffff" stroke-width="1.2"/>
          <path d="M3 4.8l5 3.6 5-3.6" fill="none" stroke="#ffffff" stroke-width="1.2"/>
        </svg>mvega_ca@inboxmail.com</li>
      <li class="contact__item contact__item--bullet"><span class="contact__dot"></span>Hablo Espanol</li>
      <li class="contact__item contact__item--bullet"><span class="contact__dot"></span>Loan packaging &amp; printing</li>
    </ul>

    <div class="divider"></div>

    <div class="brand">
      <p class="brand__name">Marisol Vega</p>
      <p class="brand__role">Certified Signing Agent</p>
    </div>

    <p class="tagline">7 days a week to meet your clients needs</p>
    <span class="chat-mark" aria-hidden="true"></span>
  </section>
</body>
</html>
```